FOOD SUPPLEMENT FOR SOAR THROAT - TELVAROSE

I need a design for a food supplement product. The product is a formulation designed to combat bacteria that causes infections in the throat. Due to the fact that is a food supplment the design has to be away from the regular farmacy products. The design has to be elegant in the same time to shows the seriousness of the product. Need to have 3 pictograms for gluten , sugar and lactose free, the photo of the ingredients is an option. As colors yellow, orange, lime green and dark blue is preferable. In attached the dimensions of the box, the logo of the name of the product and the old box where the 3 pictograms Ithe ingredients are Murraya paniculata, Vitamin C, Malva sylvestris and Filipendula ulmaria. The title under the name is Food supplement in functional chewing gum and in italian Integratore alimentare in chewing gum funzionale.

Industry/Entity Type

pharmaceutical

Colors
0054AA
0677BA
7BADD7
CADEEF
E8F1F8
59FF00
82FF00
B8FF75
E3FFCB
F4FFEA
FFF300
FFF600
FEFA6F
FFFEC7
FFFEE8
F0912C
F2A743
F7CA91
FBE8D2
FDF5EE

Requirements
Must have
• pictograms -gluten, lactose, sugar free

```html
<!DOCTYPE html>
<html lang="en">
<head>
<meta charset="utf-8">
<title>Fustella chol control – TELVAROSE</title>
<link rel="stylesheet" href="https://fonts.googleapis.com/css2?family=Open+Sans:wght@400;700&family=Barlow+Condensed:wght@800&family=Parisienne&family=Montserrat:wght@400;700&family=Fredoka:wght@400;600&display=swap">
<style>
  :root {
    --dieline: #1f4fa8;
    --navy: #233f85;
    --deep-blue: #1c3c8a;
    --sky-blue: #2b8ad4;
    --lime: #d6e22b;
    --lime-light: #eef06a;
    --leaf-green: #16a012;
    --acting-green: #3aa30f;
    --orange: #f05a14;
    --varnish-yellow: #fff200;
    --ink: #231f20;
    --white: #ffffff;
  }
  html, body {
    margin: 0;
    padding: 0;
    overflow: hidden;
    background: var(--white);
  }
  .sheet {
    position: relative;
    width: 848px;
    height: 1200px;
    overflow: hidden;
    background: var(--white);
  }
  .sheet-title {
    position: absolute;
    left: 44px;
    top: 25px;
    margin: 0;
    font: 700 45px/1 "Open Sans", sans-serif;
    color: var(--ink);
    letter-spacing: -0.5px;
  }
  .dieline-art {
    position: absolute;
    left: 0;
    top: 0;
    width: 848px;
    height: 1200px;
  }
  .cut { fill: none; stroke: var(--dieline); stroke-width: 3; stroke-linejoin: round; }
  .brand-name { font-family: "Barlow Condensed", sans-serif; font-weight: 800; fill: var(--lime); }
  .supplement-label { font-family: "Open Sans", sans-serif; font-weight: 400; fill: var(--white); }
  .tagline { font-family: "Parisienne", cursive; fill: var(--navy); }
  .count-number { font-family: "Open Sans", sans-serif; font-weight: 700; fill: var(--white); }
  .count-unit { font-family: "Open Sans", sans-serif; font-size: 16px; fill: var(--white); }
  .fast-word { font-family: "Fredoka", sans-serif; font-weight: 600; fill: var(--orange); }
  .acting-word { font-family: "Fredoka", sans-serif; font-weight: 400; fill: var(--acting-green); }
  .benefit { font-family: "Montserrat", sans-serif; font-size: 21px; fill: var(--white); }
  .claim-label { font-family: "Montserrat", sans-serif; font-size: 17px; fill: var(--white); text-anchor: middle; }
  .claim-label .strong { font-weight: 700; }
  .claim-ring { fill: none; stroke: var(--lime); stroke-width: 3; }
  .claim-slash { stroke: var(--lime); stroke-width: 3; }
  .varnish-note { font-family: "Barlow Condensed", sans-serif; font-size: 15px; fill: var(--ink); }
  .batch-note { font-family: "Montserrat", sans-serif; font-size: 13px; fill: var(--ink); }
</style>
</head>
<body>
<main class="sheet">
  <h1 class="sheet-title">FUSTELLA chol control</h1>

  <svg class="dieline-art" viewBox="0 0 1654 2339" xmlns="http://www.w3.org/2000/svg" aria-label="Die-cut box layout">
    <defs>
      <linearGradient id="front-blue" x1="0" y1="0" x2="1" y2="1">
        <stop offset="0" stop-color="#2b8ad4"/>
        <stop offset="0.55" stop-color="#2660ab"/>
        <stop offset="1" stop-color="#1e3f8c"/>
      </linearGradient>
      <radialGradient id="corner-glow" cx="1" cy="1" r="0.35">
        <stop offset="0" stop-color="#c9d6ee" stop-opacity="0.8"/>
        <stop offset="1" stop-color="#c9d6ee" stop-opacity="0"/>
      </radialGradient>

      <g id="front-panel">
        <rect x="335" y="463" width="945" height="599" fill="var(--white)"/>
        <path d="M335,730 C450,800 600,852 770,852 C1000,852 1180,782 1280,690 L1280,1062 L335,1062 Z" fill="url(#front-blue)"/>
        <rect x="1100" y="880" width="180" height="182" fill="url(#corner-glow)"/>
        <path d="M505,822 C600,850 680,858 770,858 C1000,858 1180,788 1280,700" fill="none" stroke="var(--deep-blue)" stroke-width="14"/>

        <g class="count-badge">
          <circle cx="424" cy="536" r="53" fill="var(--navy)"/>
          <text class="count-number" x="424" y="553" font-size="60" text-anchor="middle">24</text>
          <text class="count-unit" x="422" y="569" text-anchor="middle">lozenges</text>
        </g>

        <text class="brand-name" x="895" y="675" font-size="92" text-anchor="middle" textLength="455" lengthAdjust="spacingAndGlyphs">TELVAROSE</text>

        <rect x="627" y="689" width="318" height="48" rx="3" fill="var(--leaf-green)"/>
        <text class="supplement-label" x="786" y="726" font-size="32" text-anchor="middle" textLength="298" lengthAdjust="spacingAndGlyphs">FOOD SUPPLEMENT</text>
        <text class="tagline" x="866" y="792" font-size="50" text-anchor="middle">for soar throat</text>

        <g class="fast-badge">
          <circle cx="466" cy="774" r="70" fill="var(--lime)" stroke="var(--lime-light)" stroke-width="4"/>
          <circle cx="466" cy="774" r="63" fill="none" stroke="var(--lime-light)" stroke-width="2"/>
          <text class="fast-word" x="466" y="782" font-size="56" text-anchor="middle">Fast</text>
          <text class="acting-word" x="480" y="810" font-size="24" text-anchor="middle">Acting</text>
        </g>

        <text class="benefit" x="367" y="969">- Fast &amp; Effective relief for sore throats</text>
        <text class="benefit" x="367" y="999">- Antibacterial Action</text>
        <text class="benefit" x="367" y="1029">- Helps clear nasal passagers</text>

        <g class="claim claim-lactose">
          <circle class="claim-ring" cx="990" cy="968" r="25"/>
          <path d="M990,952 C982,963 978,970 978,976 A12,12 0 0 0 1002,976 C1002,970 998,963 990,952 Z" fill="var(--lime)"/>
          <line class="claim-slash" x1="973" y1="951" x2="1007" y2="985"/>
          <text class="claim-label" x="990" y="1015">LACTOSE</text>
          <text class="claim-label" x="990" y="1034"><tspan class="strong">FREE</tspan></text>
        </g>
        <g class="claim claim-gluten">
          <circle class="claim-ring" cx="1092" cy="968" r="25"/>
          <line x1="1092" y1="952" x2="1092" y2="986" stroke="var(--lime)" stroke-width="3"/>
          <line class="claim-slash" x1="1075" y1="951" x2="1109" y2="985"/>
          <text class="claim-label" x="1092" y="1015">GLUTEN</text>
          <text class="claim-label" x="1092" y="1034"><tspan class="strong">FREE</tspan></text>
        </g>
        <g class="claim claim-sugar">
          <circle class="claim-ring" cx="1193" cy="968" r="25"/>
          <rect x="1182" y="957" width="22" height="22" fill="var(--lime)"/>
          <line class="claim-slash" x1="1176" y1="951" x2="1210" y2="985"/>
          <text class="claim-label" x="1196" y="1015">SUGAR</text>
          <text class="claim-label" x="1198" y="1034"><tspan class="strong">FREE</tspan></text>
        </g>
      </g>

      <g id="side-panel">
        <rect x="370" y="1128" width="388" height="47" rx="3" fill="var(--leaf-green)"/>
        <text class="supplement-label" x="564" y="1167" font-size="40" text-anchor="middle" textLength="366" lengthAdjust="spacingAndGlyphs">FOOD SUPPLEMENT</text>
        <text class="tagline" x="597" y="1228" font-size="50" text-anchor="middle">for soar throat</text>
        <text class="brand-name" x="1088" y="1195" font-size="56" text-anchor="middle" textLength="252" lengthAdjust="spacingAndGlyphs">TELVAROSE</text>
      </g>
    </defs>

    <use href="#front-panel"/>
    <use href="#front-panel" transform="translate(-3,795)"/>
    <use href="#side-panel"/>
    <use href="#side-panel" transform="translate(0,800)"/>

    <g class="glue-panel-notes">
      <rect x="1328" y="733" width="84" height="169" fill="var(--varnish-yellow)"/>
      <text class="varnish-note" transform="translate(1378,862) rotate(-90)">RISERVA VERNICE</text>
      <text class="batch-note" transform="translate(1352,1035) rotate(-90)">Lotto:</text>
      <text class="batch-note" transform="translate(1374,1035) rotate(-90)">Da consumarsi</text>
      <text class="batch-note" transform="translate(1390,1035) rotate(-90)">preferibilmente</text>
      <text class="batch-note" transform="translate(1406,1035) rotate(-90)">entro:</text>
    </g>

    <g class="cut-lines">
      <path class="cut" d="M335,463 L368,337 L1243,337 L1278,463"/>
      <rect class="cut" x="335" y="463" width="945" height="597"/>
      <path class="cut" d="M1280,463 L1480,463 L1480,1058 L1280,1058"/>
      <path class="cut" d="M1480,467 L1500,467 C1545,467 1572,495 1572,525 L1572,1000 C1572,1030 1545,1055 1500,1055 L1480,1055"/>
      <path class="cut" d="M1480,510 L1470,510 L1470,1012 L1480,1012"/>

      <path class="cut" d="M335,1064 L305,1064 L288,1082 L180,1112 L180,1228 L315,1240 L335,1258"/>
      <path class="cut" d="M1278,1062 L1298,1078 L1432,1090 L1432,1207 L1325,1236 L1305,1254 L1278,1254"/>
      <line class="cut" x1="1278" y1="1060" x2="1278" y2="1258"/>
      <line class="cut" x1="330" y1="1258" x2="1278" y2="1258"/>

      <path class="cut" d="M330,1260 L130,1260 L130,1263 L100,1263 C62,1265 40,1295 40,1330 L40,1800 C40,1830 62,1852 100,1852 L130,1852 L130,1855 L330,1855"/>
      <path class="cut" d="M130,1305 L140,1305 L140,1810 L130,1810"/>
      <rect class="cut" x="330" y="1258" width="948" height="597"/>

      <path class="cut" d="M335,1857 L315,1875 L180,1887 L180,2003 L288,2033 L305,2050 L335,2050"/>
      <path class="cut" d="M1278,1860 L1305,1860 L1325,1878 L1432,1908 L1432,2027 L1298,2035 L1282,2050"/>
      <line class="cut" x1="335" y1="1855" x2="335" y2="2050"/>
      <line class="cut" x1="1278" y1="1855" x2="1278" y2="2050"/>
      <line class="cut" x1="305" y1="2050" x2="1282" y2="2050"/>

      <path d="M1262,445 L1272,438 L1272,452 Z" fill="var(--dieline)"/>
      <path d="M1258,1240 L1268,1233 L1268,1247 Z" fill="var(--dieline)"/>
    </g>
  </svg>
</main>
</body>
</html>
```